A gang member and street hustler turned preacher needs a cover

A man who used to be a gang member and street hustler turned his life around and became a preacher. He has written a book titled Unsteepled: My Passage From Ashes to Glory and he needs a cover for the book. The book is a memoir about his life and his journey from the streets to the church. It details the lessons that he's learned along the way. I have attached a photo to incorporate in the cover design. <br/>Title: Unsteepled: My Passage From Ashes to Glory<br/>Author: Dr. Malcolm T. Hayward

```html
<!DOCTYPE html>
<html lang="en">
<head>
<meta charset="utf-8">
<title>Unsteepled: My Passage From Ashes to Glory — Book Cover</title>
<link rel="stylesheet" href="https://fonts.googleapis.com/css2?family=Oswald:wght@500&family=Cinzel:wght@400;600&display=swap">
<style>
  :root {
    --page-bg: #ffffff;
    --cover-black: #050505;
    --photo-mid: #2a2a2a;
    --photo-dark: #0b0b0b;
    --gold-light: #f3e3a6;
    --gold-mid: #c9a24f;
    --gold-deep: #8c6a2a;
    --band-ink: #1a1409;
    --subtitle-ink: #f4f0e6;
    --rule: #6b6b6b;
  }
  html, body {
    margin: 0;
    padding: 0;
    width: 1200px;
    height: 1200px;
    overflow: hidden;
    background: var(--page-bg);
  }
  .book-cover {
    position: absolute;
    left: 214px;
    top: 22px;
    width: 772px;
    height: 1156px;
    background: var(--cover-black);
  }
  .book-cover svg { display: block; }
  .title-main { font-family: "Oswald", "Arial Narrow", sans-serif; font-weight: 500; }
  .title-serif { font-family: "Cinzel", "Times New Roman", serif; font-weight: 400; }
  .subtitle-lead { font-family: "Cinzel", "Times New Roman", serif; font-weight: 400; fill: var(--subtitle-ink); }
  .author-name { font-family: "Cinzel", "Times New Roman", serif; font-weight: 600; fill: var(--band-ink); }
</style>
</head>
<body>
<main class="book-cover">
  <svg width="772" height="1156" viewBox="0 0 772 1156">
    <defs>
      <radialGradient id="portraitTone" cx="50%" cy="42%" r="60%">
        <stop offset="0%" stop-color="var(--photo-mid)"/>
        <stop offset="55%" stop-color="var(--photo-dark)"/>
        <stop offset="100%" stop-color="var(--cover-black)"/>
      </radialGradient>
      <linearGradient id="goldText" x1="0" y1="0" x2="1" y2="0.3">
        <stop offset="0%" stop-color="var(--gold-deep)"/>
        <stop offset="35%" stop-color="var(--gold-light)"/>
        <stop offset="65%" stop-color="var(--gold-mid)"/>
        <stop offset="100%" stop-color="var(--gold-deep)"/>
      </linearGradient>
      <linearGradient id="goldBand" x1="0" y1="0" x2="1" y2="0">
        <stop offset="0%" stop-color="var(--gold-deep)"/>
        <stop offset="30%" stop-color="var(--gold-light)"/>
        <stop offset="60%" stop-color="var(--gold-mid)"/>
        <stop offset="100%" stop-color="var(--gold-deep)"/>
      </linearGradient>
    </defs>

    <rect class="author-portrait" x="0" y="0" width="772" height="1056" fill="url(#portraitTone)"
          role="img" aria-label="Dark portrait of the author in a suit, hands clasped, with broken shackles framing the title"/>

    <text class="title-main" x="62" y="212" font-size="152" textLength="654" lengthAdjust="spacingAndGlyphs" fill="url(#goldText)">UNSTEEPLED</text>

    <line x1="62" y1="330" x2="176" y2="330" stroke="var(--rule)" stroke-width="2"/>
    <line x1="596" y1="330" x2="710" y2="330" stroke="var(--rule)" stroke-width="2"/>
    <text class="subtitle-lead" x="386" y="341" font-size="31" text-anchor="middle">My Passage From</text>

    <text class="title-serif" x="386" y="482" font-size="140" text-anchor="middle" fill="url(#goldText)">ASHES</text>
    <text class="subtitle-lead" x="386" y="564" font-size="30" text-anchor="middle">TO</text>
    <text class="title-serif" x="415" y="704" font-size="116" textLength="466" lengthAdjust="spacingAndGlyphs" text-anchor="middle" fill="url(#goldText)">GLORY</text>

    <rect class="author-band" x="0" y="1056" width="772" height="100" fill="url(#goldBand)"/>
    <text class="author-name" x="386" y="1124" font-size="48" text-anchor="middle" textLength="600" lengthAdjust="spacingAndGlyphs">DR. MALCOLM T. HAYWARD</text>
  </svg>
</main>
</body>
</html>
```